Car rental website design for a UAE car rental company

This project is about creating a new website design for a car rental company located in Dubai (United Arab Emirates), I opened the same project a few months ago but I didn't receive a lot of appealing entries so I closed it but this time I am marking the project as guaranteed to avoid such situation again, if you have already provided a design before then please re-submit again on this project so that it is considered while reviewing all the designs

A few important things:

1- We need a simple non-complex design
2- The final deliverable would be 2 screens (PSD, JPEG ... etc), the first screen is for the home page and the second screen is for an internal page
3- The home page must have a section that end users can use to rent a car online directly from the home page instead of going into some inner pages
4- The current website is very old and not very appealing so avoid creating a similar design (www.quarvin-drive.example)
5- The name is Quarvin but the company rents normal cars (no Limousin cars will be rented) so avoid adding any fancy cars in the images/graphics used in the design, just normal end users cars
6- The expected pages would be: home, About us, Our team, Strategy, Contact us and links to social media pages
7- The attachments include the company's logo and some screens from other car rental companies that provide online rentals/payments

If you have any questions please feel free to ask and please note that we will need the designs urgently

Thanks

Target Market(s)

Dubai - United Arab Emirates

Industry/Entity Type

It Company

Number of Pages Required

2 page

Font styles to use
Sans Serif

Requirements
Must have
• Check the project details
Nice to have
Should not have

```html
<!DOCTYPE html>
<html lang="en">
<head>
<meta charset="utf-8">
<title>Quarvin – Rent A Car in Dubai</title>
<link rel="stylesheet" href="https://fonts.googleapis.com/css2?family=Archivo+Black&family=Arimo:wght@400;700&family=Jost:wght@300;400;500&display=swap">
<style>
  :root {
    --brand-red: #a0093c;
    --brand-red-dark: #86062f;
    --page-bg: #e7e7e7;
    --text-dark: #3f3f3f;
    --text-mid: #5c5c5c;
    --text-soft: #7a7a7a;
    --icon-grey: #8a8a8a;
    --band-sage: #8b9a93;
    --logo-grey: #7f8c86;
    --white: #ffffff;
    --field-bg: rgba(120, 120, 120, 0.55);
    --panel-bg: rgba(40, 40, 40, 0.45);
    --line-dots: #a5a5a5;
  }
  * { margin: 0; padding: 0; box-sizing: border-box; }
  html, body { width: 804px; height: 1200px; overflow: hidden; }
  body {
    position: relative;
    background: var(--page-bg);
    font-family: "Arimo", Arial, sans-serif;
    color: var(--text-mid);
  }
  .abs { position: absolute; }

  /* Hero */
  .hero-photo {
    position: absolute; left: 0; top: 0; width: 804px; height: 455px;
    background: linear-gradient(180deg, #6f8fb8 0%, #9fb3cc 22%, #7d7f8c 42%, #5b4a3e 58%, #b8863c 72%, #3f4a5c 84%, #d9a648 100%);
  }
  .brand {
    position: absolute; display: flex; align-items: center; gap: 8px;
    font-family: "Jost", sans-serif; font-weight: 400; color: var(--logo-grey);
  }
  .brand-mark { width: 14px; height: 14px; background: var(--brand-red); }
  .brand--header { left: 105px; top: 50px; font-size: 26px; }
  .brand--footer { left: 592px; top: 1080px; font-size: 26px; }

  .phone-support {
    right: 228px; top: 27px; font-size: 9px; font-weight: 700; color: var(--white);
    white-space: nowrap; text-align: right;
  }
  .social { display: flex; gap: 4px; }
  .social span {
    width: 19px; height: 19px; border: 1.5px solid var(--brand-red); background: var(--white);
    display: block; position: relative;
  }
  .social span::after {
    content: ""; position: absolute; inset: 3px; background: #3b5b96;
  }
  .social--top { left: 586px; top: 22px; }
  .social--top span:nth-child(2)::after { background: #2aa7d9; }
  .social--top span:nth-child(3)::after { background: #1f6fa6; }
  .social--top span:nth-child(4)::after { background: #c9382a; }
  .social--top span:nth-child(5)::after { background: #f29a1f; }
  .social--bottom { left: 586px; top: 1173px; }
  .social--bottom span { border: 1px solid #9a9a9a; background: #f4f4f4; }
  .social--bottom span::after { background: #8a8a8a; }

  .main-nav { left: 441px; top: 63px; display: flex; gap: 22px; font-size: 9.5px; color: var(--white); }
  .main-nav a { color: inherit; text-decoration: none; }
  .main-nav a.is-active { color: var(--brand-red); }

  .hero-title {
    left: 105px; top: 126px; width: 594px;
    font-family: "Archivo Black", sans-serif; font-size: 28.5px; font-weight: 400; color: rgba(255,255,255,.92);
    letter-spacing: 1px; white-space: nowrap;
  }

  /* Booking panel */
  .booking { left: 105px; top: 169px; width: 594px; height: 196px; background: var(--panel-bg); }
  .booking-bar {
    height: 33px; background: var(--brand-red); display: flex; align-items: center; position: relative;
  }
  .booking-bar h2 {
    font-size: 12.5px; font-weight: 700; color: var(--white); letter-spacing: .6px;
    width: 107px; padding-left: 10px; height: 100%; display: flex; align-items: center;
    border-right: 1px solid rgba(255,255,255,.25);
  }
  .booking-bar a { color: var(--white); font-size: 8.5px; margin-left: 13px; text-decoration: none; }
  .booking-bar .globe { position: absolute; right: 10px; top: 7px; }
  .field-label { font-size: 8.8px; font-weight: 700; color: var(--white); }
  .field {
    height: 25px; background: var(--field-bg); color: #e6e6e6; font-size: 8.5px;
    display: flex; align-items: center; justify-content: space-between; padding: 0 8px;
  }
  .quote-btn {
    left: 583px; top: 322px; width: 103px; height: 31px; background: var(--brand-red);
    color: var(--white); font-size: 11.5px; font-weight: 700; display: flex; align-items: center; justify-content: center;
    letter-spacing: .4px;
  }

  .fleet-photo {
    left: 103px; top: 403px; width: 596px; height: 95px; border-radius: 40px 40px 10px 10px;
    background: linear-gradient(90deg, #8fa8c8 0%, #c9262f 22%, #d4d6d8 46%, #c71d2c 70%, #5f6064 100%);
    opacity: .9;
  }

  .divider { left: 105px; width: 594px; border-top: 1px dashed var(--line-dots); }

  .section-title {
    left: 105px; width: 594px; text-align: center;
    font-family: "Jost", sans-serif; font-weight: 300; color: var(--text-dark); letter-spacing: .5px;
  }
  .welcome-title { top: 543px; font-size: 21px; }
  .welcome-text { left: 105px; top: 587px; width: 594px; text-align: center; font-size: 8.6px; line-height: 10.5px; color: var(--text-mid); }
  .welcome-text p + p { margin-top: 10px; }
  .read-more {
    left: 344px; top: 650px; width: 113px; height: 22px; background: var(--brand-red);
    color: var(--white); font-size: 9px; font-weight: 700; display: flex; align-items: center; justify-content: center;
  }

  .services-title { top: 729px; font-size: 17px; }
  .services-intro { left: 105px; top: 775px; width: 182px; font-size: 8.6px; line-height: 10.5px; color: var(--text-dark); }
  .services-photo {
    left: 107px; top: 842px; width: 172px; height: 60px; border-radius: 22px 22px 8px 8px;
    background: linear-gradient(90deg, #1e1e1e 0%, #3a3a3a 40%, #c42a24 62%, #a51b1b 100%);
  }
  .service { display: flex; align-items: flex-start; gap: 7px; font-size: 8.6px; line-height: 10px; color: var(--text-soft); }
  .service svg { flex: none; }

  /* Signup */
  .signup { left: 105px; top: 938px; width: 594px; height: 52px; background: var(--band-sage); }
  .signup-text {
    left: 116px; top: 954px; font-family: "Jost", sans-serif; font-size: 12.5px; color: var(--white);
  }
  .signup-field {
    top: 951px; width: 123px; height: 27px; background: var(--white); font-size: 7.5px; color: #8c8c8c;
    padding-left: 13px; display: flex; align-items: center;
  }
  .signup-btn {
    left: 626px; top: 951px; width: 60px; height: 27px; background: var(--brand-red); color: var(--white);
    font-size: 9px; font-weight: 700; display: flex; align-items: center; justify-content: center;
  }

  /* Footer */
  .site-footer { left: 0; top: 1021px; width: 800px; height: 142px; background: var(--white); }
  .footer-heading { top: 1046px; font-family: "Jost", sans-serif; font-size: 12px; font-weight: 400; color: var(--text-dark); }
  .footer-list { top: 1075px; list-style: none; font-size: 7.5px; line-height: 12.4px; color: var(--text-mid); }
  .bottom-bar { left: 0; top: 1163px; width: 804px; height: 37px; background: #ececec; border-top: 2px solid #d4d4d4; }
  .copyright { left: 105px; top: 1178px; font-size: 7.5px; font-weight: 400; color: var(--text-mid); letter-spacing: .3px; }
</style>
</head>
<body>

<header>
  <div class="hero-photo" role="img" aria-label="Dubai skyline at dusk with the tower and lit highways along the waterfront"></div>

  <div class="brand brand--header"><span class="brand-mark"></span>Quarvin</div>

  <div class="abs phone-support">PHONE SUPPORT +971 4 555 0147</div>
  <div class="abs social social--top" aria-label="Social media links"><span></span><span></span><span></span><span></span><span></span></div>

  <nav class="abs main-nav">
    <a class="is-active" href="#">Home</a>
    <a href="#">About us</a>
    <a href="#">Our team</a>
    <a href="#">Strategy</a>
    <a href="#">Contact us</a>
  </nav>

  <h1 class="abs hero-title">FIND BEST RENTAL CARS IN DUBAI</h1>

  <section class="abs booking">
    <div class="booking-bar">
      <h2>BOOK A CAR</h2>
      <a href="#">View Modify or Cancel a Booking</a>
      <svg class="globe" width="19" height="19" viewBox="0 0 20 20"><circle cx="10" cy="10" r="9" fill="#fff"/><path d="M6 5c2 1 3 3 2 5s-3 2-3 4M12 4c-1 2 1 3 3 4s1 4-1 6" stroke="#a0093c" stroke-width="2" fill="none"/></svg>
    </div>
  </section>

  <div class="abs field-label" style="left:117px;top:216px">Picking Up Location</div>
  <div class="abs field" style="left:117px;top:231px;width:264px">Airport or Anywhere
    <svg width="9" height="12" viewBox="0 0 9 12"><path d="M4.5 0a4.5 4.5 0 0 1 4.5 4.5C9 8 4.5 12 4.5 12S0 8 0 4.5A4.5 4.5 0 0 1 4.5 0z" fill="#fff"/><circle cx="4.5" cy="4.5" r="1.7" fill="#888"/></svg></div>
  <div class="abs field-label" style="left:394px;top:216px">Picking Up Date</div>
  <div class="abs field" style="left:394px;top:231px;width:151px">dd/mm/yyyy
    <svg width="14" height="14" viewBox="0 0 14 14"><rect x=".5" y="2" width="13" height="11.5" fill="none" stroke="#fff"/><path d="M.5 5h13M4 8h2M8 8h2M4 11h2M8 11h2" stroke="#fff"/></svg></div>
  <div class="abs field-label" style="left:558px;top:216px">Picking Up Hour</div>
  <div class="abs field" style="left:558px;top:231px;width:124px">dd/mm/yyyy
    <svg width="14" height="14" viewBox="0 0 14 14"><circle cx="7" cy="7" r="6" fill="none" stroke="#fff" stroke-width="1.4"/><path d="M7 3.5V7h3" stroke="#fff" stroke-width="1.4" fill="none"/></svg></div>

  <div class="abs field-label" style="left:117px;top:264px">Droping Off Location</div>
  <div class="abs field" style="left:117px;top:279px;width:264px">Airport or Anywhere
    <svg width="9" height="12" viewBox="0 0 9 12"><path d="M4.5 0a4.5 4.5 0 0 1 4.5 4.5C9 8 4.5 12 4.5 12S0 8 0 4.5A4.5 4.5 0 0 1 4.5 0z" fill="#fff"/><circle cx="4.5" cy="4.5" r="1.7" fill="#888"/></svg></div>
  <div class="abs field-label" style="left:394px;top:264px">Droping Off Date</div>
  <div class="abs field" style="left:394px;top:279px;width:151px">dd/mm/yyyy
    <svg width="14" height="14" viewBox="0 0 14 14"><rect x=".5" y="2" width="13" height="11.5" fill="none" stroke="#fff"/><path d="M.5 5h13M4 8h2M8 8h2M4 11h2M8 11h2" stroke="#fff"/></svg></div>
  <div class="abs field-label" style="left:558px;top:264px">Droping Off Hour</div>
  <div class="abs field" style="left:558px;top:279px;width:124px">dd/mm/yyyy
    <svg width="14" height="14" viewBox="0 0 14 14"><circle cx="7" cy="7" r="6" fill="none" stroke="#fff" stroke-width="1.4"/><path d="M7 3.5V7h3" stroke="#fff" stroke-width="1.4" fill="none"/></svg></div>

  <div class="abs quote-btn">GET A QUOTE</div>

  <div class="abs fleet-photo" role="img" aria-label="Row of five everyday hatchbacks in blue, red, silver, red and grey"></div>
</header>

<main>
  <div class="abs divider" style="top:519px"></div>
  <h2 class="abs section-title welcome-title">WELCOME TO QUARVIN</h2>
  <div class="abs welcome-text">
    <p>As Dubai is expected to welcome millions of tourists and visitors, car rental industry is believed to escalate more rapidly in the region.</p>
    <p>Over the past five years, demands for car rentals in Dubai has been augmenting at a healthy pace and is currently registering a growth rate of<br>20 to 25 percent per year. The swift economic growth and the number</p>
  </div>
  <div class="abs read-more">READ MORE</div>

  <div class="abs divider" style="top:704px"></div>
  <h2 class="abs section-title services-title">OUR SERVICES</h2>

  <p class="abs services-intro">Quarvin offers a comprehensive range of services including daily, short term and long term rental, chauffeur drive services for every purpose and budget.</p>
  <div class="abs services-photo" role="img" aria-label="Black sedan and red coupe side by side"></div>

  <div class="abs service" style="left:321px;top:775px;width:190px">
    <svg width="14" height="12" viewBox="0 0 14 12"><path d="M2 6l1.5-4h7L12 6h1v4h-2v1.5H9V10H5v1.5H3V10H1V6z" fill="#8a8a8a"/></svg>
    <span>Wide range of vehicles for city driving or SUV's for trips</span></div>
  <div class="abs service" style="left:321px;top:817px;width:190px">
    <svg width="14" height="14" viewBox="0 0 14 14"><path d="M1 7l6-6h6v6l-6 6z" fill="#8a8a8a"/><circle cx="10" cy="4" r="1.3" fill="#e7e7e7"/></svg>
    <span>Special 10% discount for new customers on the first rent</span></div>
  <div class="abs service" style="left:321px;top:858px;width:190px">
    <svg width="14" height="14" viewBox="0 0 14 14"><circle cx="7" cy="7" r="6.5" fill="#8a8a8a"/><path d="M7 3v4h3" stroke="#e7e7e7" stroke-width="1.4" fill="none"/></svg>
    <span style="padding-top:2px">Long term car rental</span></div>
  <div class="abs service" style="left:321px;top:892px;width:190px">
    <svg width="14" height="12" viewBox="0 0 14 12"><path d="M6 0L0 5l6 5V7c4 0 6 1 8 5 0-5-3-8-8-8z" fill="#8a8a8a"/></svg>
    <span>Buyback option after lease term</span></div>

  <div class="abs service" style="left:539px;top:777px;width:160px">
    <svg width="16" height="12" viewBox="0 0 16 12"><rect x="1" y="3" width="9" height="6" rx="3" transform="rotate(-30 5 6)" fill="#8a8a8a"/><circle cx="12" cy="7" r="3.5" fill="#8a8a8a"/></svg>
    <span>Special offers for online bookings</span></div>
  <div class="abs service" style="left:541px;top:817px;width:160px">
    <svg width="12" height="15" viewBox="0 0 12 15"><rect x="3" y="0" width="6" height="3" fill="#8a8a8a"/><circle cx="6" cy="5" r="2.5" fill="#8a8a8a"/><path d="M1 15v-5l5-2 5 2v5z" fill="#8a8a8a"/></svg>
    <span style="padding-top:2px">Chauffer drive service</span></div>
  <div class="abs service" style="left:539px;top:858px;width:160px">
    <svg width="16" height="15" viewBox="0 0 16 15"><path d="M15 1L1 7l5 1 1 6 2-4 4 1z" fill="#8a8a8a"/></svg>
    <span style="padding-top:2px">Airport transfers</span></div>
  <div class="abs service" style="left:541px;top:889px;width:160px">
    <svg width="14" height="16" viewBox="0 0 14 16"><path d="M4 16V4h2V0h1v4h2v12zM1 16V10h2v6zM10 16V8h3v8z" fill="#8a8a8a"/></svg>
    <span style="padding-top:3px">sightseeing tours</span></div>

  <div class="abs signup"></div>
  <div class="abs signup-text">Signup for our email to celebrate great specials</div>
  <div class="abs signup-field" style="left:370px">Name</div>
  <div class="abs signup-field" style="left:498px">Email</div>
  <div class="abs signup-btn">SIGNUP</div>
</main>

<footer>
  <div class="abs site-footer"></div>

  <h3 class="abs footer-heading" style="left:105px">Quick Links</h3>
  <ul class="abs footer-list" style="left:105px">
    <li>Home</li><li>About us</li><li>Our team</li><li>Strategy</li>
  </ul>

  <h3 class="abs footer-heading" style="left:253px">Support</h3>
  <ul class="abs footer-list" style="left:253px">
    <li>Contact Us</li><li>Find Your Invois</li><li>FAQ</li>
  </ul>

  <h3 class="abs footer-heading" style="left:401px">Contact Us</h3>
  <ul class="abs footer-list" style="left:402px">
    <li>P.O. Box 48210 Dubai, UAE</li>
    <li>Tel: +971 4 555 0147</li>
    <li>Fax: +971 4 555 0148</li>
    <li>Email: info@quarvin-drive.example</li>
    <li>URL: www.quarvin-drive.example</li>
  </ul>

  <div class="brand brand--footer"><span class="brand-mark"></span>Quarvin</div>

  <div class="abs bottom-bar"></div>
  <div class="abs copyright">©Copyright 2015, Quarvin. All rights reserved.</div>
  <div class="abs social social--bottom" aria-label="Social media links"><span></span><span></span><span></span><span></span><span></span></div>
</footer>

</body>
</html>
```